Acai Label - 2oz

I'm going to need a graphic label for 2oz Amble Glass bottle. My company is Brisk Harbor and this particular product is an energy shot. (organic). Please see attachments for example.
Dimensions of Bottle - I need a full wrap concept
Color: Amber
Size: 2 oz
Material: Glass
Case Pack: 240
Neck finish: 20-400
Height: 3.687 in / 9.365 cm
Diameter: 1.52 in / 3.861 cm
Label Dimensions: 4.625 x 1.75 in
Print Dimensions: 4.75 x 1.75 in
Please incorporate existing Brisk Harbor Logo on label.
Target Market(s)
Target market is - people that are interested natural forms of an energy boost.
Ages from 16- 40. I'd like it to appeal to broad spectrum of people. Please submit all creative designs and refinement can always come after.
Industry/Entity Type
It Company

```html
<!DOCTYPE html>
<html lang="en">
<head>
<meta charset="utf-8">
<title>Brisk Harbor Organic Energy – Acai 2 oz Label</title>
<link rel="stylesheet" href="https://fonts.googleapis.com/css2?family=Oswald:wght@500;600;700&display=swap">
<style>
  :root {
    --bg-top: #ffffff;
    --bg-bottom: #e4e4e4;
    --purple-light: #b06aa8;
    --purple-mid: #9a4f95;
    --purple-dark: #763a82;
    --cap-green: #5fc63c;
    --cap-green-dark: #3f9f2a;
    --leaf-green: #49ad35;
    --leaf-green-dark: #2d7f22;
    --headline-green: #3caa2e;
    --berry-dark: #2a1530;
    --berry-mid: #4b2a55;
    --pink: #e0187f;
    --white: #ffffff;
  }
  * { box-sizing: border-box; margin: 0; padding: 0; }
  html, body { width: 1200px; height: 1200px; overflow: hidden; }
  body {
    background: linear-gradient(180deg, var(--bg-top) 0%, var(--bg-top) 55%, var(--bg-bottom) 100%);
    font-family: "Oswald", "Arial Narrow", sans-serif;
    position: relative;
  }
  .bottle {
    position: absolute;
    top: 60px;
    width: 400px;
    height: 1090px;
  }
  .bottle--ribbon { left: 76px; }
  .bottle--fruit { left: 676px; }
  .bottle__shape { position: absolute; inset: 0; width: 400px; height: 1090px; }

  .brand {
    position: absolute;
    top: 300px; left: 0; width: 400px;
    text-align: center;
    color: var(--white);
  }
  .brand__name {
    display: inline-flex; align-items: center; gap: 10px;
    font-weight: 500; font-size: 34px; letter-spacing: 1px;
  }
  .brand__dot { width: 16px; height: 16px; border-radius: 50%; background: var(--white); }
  .brand__tagline {
    display: block; margin-top: 2px;
    font-weight: 500; font-size: 11px; letter-spacing: 3px;
  }

  .headline {
    position: absolute;
    top: 418px; left: 0; width: 400px;
    text-align: center;
    color: var(--white);
    font-weight: 600;
    font-size: 84px;
    line-height: 88px;
    letter-spacing: -1px;
    text-shadow:
      2px 2px 0 var(--headline-green), -2px -2px 0 var(--headline-green),
      2px -2px 0 var(--headline-green), -2px 2px 0 var(--headline-green),
      3px 0 0 var(--headline-green), -3px 0 0 var(--headline-green),
      0 3px 0 var(--headline-green), 0 -3px 0 var(--headline-green),
      0 6px 8px rgba(40, 20, 50, 0.45);
  }

  .fruit-window {
    position: absolute;
    left: 86px; top: 654px;
    width: 228px; height: 228px;
    border-radius: 50%;
    border: 9px solid var(--white);
    background: radial-gradient(circle at 40% 35%, var(--berry-mid) 0%, var(--berry-dark) 70%);
    box-shadow: 0 4px 10px rgba(0,0,0,0.3);
  }
  .flavor-ribbon {
    position: absolute;
    left: 68px; top: 852px;
    width: 300px; height: 48px;
    background: var(--pink);
    color: var(--white);
    font-weight: 600; font-size: 32px; line-height: 48px;
    text-align: center;
    box-shadow: 0 3px 6px rgba(0,0,0,0.25);
  }

  .fruit-art {
    position: absolute;
    left: 50px; top: 650px;
    width: 320px; height: 226px;
    border-radius: 50%;
    background: radial-gradient(ellipse at 50% 50%, var(--berry-dark) 0%, var(--berry-mid) 35%, rgba(73,173,53,0.75) 60%, rgba(154,79,149,0) 72%);
  }
  .flavor-name {
    position: absolute;
    top: 900px; left: 0; width: 400px;
    text-align: center;
    color: var(--pink);
    font-weight: 600; font-size: 34px; line-height: 40px;
  }

  .claims {
    position: absolute;
    top: 948px; left: 0; width: 400px;
    text-align: center;
    color: var(--white);
    text-shadow: 0 2px 3px rgba(0,0,0,0.35);
  }
  .claims__main { display: block; font-weight: 600; font-size: 38px; line-height: 44px; }
  .claims__sub { display: block; font-weight: 500; font-size: 16px; line-height: 18px; }
  .claims__volume { display: block; margin-top: 10px; font-weight: 600; font-size: 36px; line-height: 40px; }

  .cert-badge {
    position: absolute;
    left: 336px; top: 940px;
    width: 52px; height: 52px;
    border-radius: 50%;
    background: var(--white);
    border: 4px solid var(--leaf-green-dark);
  }
</style>
</head>
<body>

<div class="bottle bottle--ribbon">
  <svg class="bottle__shape" viewBox="0 0 400 1090" aria-hidden="true">
    <defs>
      <linearGradient id="glass-a" x1="0" y1="0" x2="0" y2="1">
        <stop offset="0" stop-color="var(--purple-light)"/>
        <stop offset="0.5" stop-color="var(--purple-mid)"/>
        <stop offset="1" stop-color="var(--purple-dark)"/>
      </linearGradient>
      <linearGradient id="cap-a" x1="0" y1="0" x2="0" y2="1">
        <stop offset="0" stop-color="var(--cap-green-dark)"/>
        <stop offset="0.35" stop-color="var(--cap-green)"/>
        <stop offset="1" stop-color="var(--cap-green-dark)"/>
      </linearGradient>
      <linearGradient id="leaf-a" x1="0" y1="0" x2="0" y2="1">
        <stop offset="0" stop-color="var(--leaf-green)"/>
        <stop offset="1" stop-color="var(--leaf-green-dark)"/>
      </linearGradient>
      <clipPath id="body-a">
        <path d="M70 130 L330 130 C330 170 320 190 325 210 C340 260 392 280 392 360 L392 1060 Q392 1090 362 1090 L38 1090 Q8 1090 8 1060 L8 360 C8 280 60 260 75 210 C80 190 70 170 70 130 Z"/>
      </clipPath>
    </defs>
    <path d="M70 130 L330 130 C330 170 320 190 325 210 C340 260 392 280 392 360 L392 1060 Q392 1090 362 1090 L38 1090 Q8 1090 8 1060 L8 360 C8 280 60 260 75 210 C80 190 70 170 70 130 Z" fill="url(#glass-a)"/>
    <rect x="0" y="900" width="400" height="190" fill="url(#leaf-a)" clip-path="url(#body-a)" role="img" aria-label="Band of green leaves with acai berries"/>
    <path d="M46 20 Q46 0 70 0 L330 0 Q354 0 354 20 L354 118 Q354 135 335 135 L65 135 Q46 135 46 118 Z" fill="url(#cap-a)"/>
    <rect x="46" y="28" width="308" height="4" fill="var(--cap-green-dark)" opacity="0.5"/>
  </svg>

  <div class="brand">
    <span class="brand__name"><span class="brand__dot"></span>Brisk Harbor</span>
    <span class="brand__tagline">ENERGY BOOST</span>
  </div>
  <h1 class="headline">ORGANIC<br>ENERGY</h1>
  <div class="fruit-window" role="img" aria-label="Close-up photo of ripe acai berries"></div>
  <div class="flavor-ribbon">ACAI</div>
  <p class="claims">
    <span class="claims__main">ALL NATURAL</span>
    <span class="claims__sub">ZERO CALORIES- SUGAR FREE</span>
    <span class="claims__volume">2 OZ (59ML)</span>
  </p>
  <div class="cert-badge" aria-hidden="true"></div>
</div>

<div class="bottle bottle--fruit">
  <svg class="bottle__shape" viewBox="0 0 400 1090" aria-hidden="true">
    <defs>
      <linearGradient id="glass-b" x1="0" y1="0" x2="0" y2="1">
        <stop offset="0" stop-color="var(--purple-light)"/>
        <stop offset="0.5" stop-color="var(--purple-mid)"/>
        <stop offset="1" stop-color="var(--purple-dark)"/>
      </linearGradient>
      <linearGradient id="cap-b" x1="0" y1="0" x2="0" y2="1">
        <stop offset="0" stop-color="var(--cap-green-dark)"/>
        <stop offset="0.35" stop-color="var(--cap-green)"/>
        <stop offset="1" stop-color="var(--cap-green-dark)"/>
      </linearGradient>
      <linearGradient id="leaf-b" x1="0" y1="0" x2="0" y2="1">
        <stop offset="0" stop-color="var(--leaf-green)"/>
        <stop offset="1" stop-color="var(--leaf-green-dark)"/>
      </linearGradient>
      <clipPath id="body-b">
        <path d="M70 130 L330 130 C330 170 320 190 325 210 C340 260 392 280 392 360 L392 1060 Q392 1090 362 1090 L38 1090 Q8 1090 8 1060 L8 360 C8 280 60 260 75 210 C80 190 70 170 70 130 Z"/>
      </clipPath>
    </defs>
    <path d="M70 130 L330 130 C330 170 320 190 325 210 C340 260 392 280 392 360 L392 1060 Q392 1090 362 1090 L38 1090 Q8 1090 8 1060 L8 360 C8 280 60 260 75 210 C80 190 70 170 70 130 Z" fill="url(#glass-b)"/>
    <rect x="0" y="900" width="400" height="190" fill="url(#leaf-b)" clip-path="url(#body-b)" role="img" aria-label="Band of green leaves with acai berries"/>
    <path d="M46 20 Q46 0 70 0 L330 0 Q354 0 354 20 L354 118 Q354 135 335 135 L65 135 Q46 135 46 118 Z" fill="url(#cap-b)"/>
    <rect x="46" y="28" width="308" height="4" fill="var(--cap-green-dark)" opacity="0.5"/>
  </svg>

  <div class="brand">
    <span class="brand__name"><span class="brand__dot"></span>Brisk Harbor</span>
    <span class="brand__tagline">ENERGY BOOST</span>
  </div>
  <h1 class="headline">ORGANIC<br>ENERGY</h1>
  <div class="fruit-art" role="img" aria-label="Illustration of three acai berries with green leaves"></div>
  <p class="flavor-name">ACAI</p>
  <p class="claims">
    <span class="claims__main">ALL NATURAL</span>
    <span class="claims__sub">ZERO CALORIES- SUGAR FREE</span>
    <span class="claims__volume">2 OZ (59ML)</span>
  </p>
  <div class="cert-badge" aria-hidden="true"></div>
</div>

</body>
</html>
```